Graphics Design for Home Page of MORVA Agency Website

+Our Business Profile+
Our company, MORVA Agency, generates income primarily by matching tutors to students. Another avenue of income comes from the advertising in our site. The website is an integral part of our marketing strategy and platform to interface with customers.

*Contest Requirements*
Our purpose is to create an interface for our website that is superior to our competitors. We have provide our home page interface template for our graphics designer to work on.

Contestants are only required to do the graphics design portion of our front page based on our template. Graphics designs are required and not random photos and clip art to be inserted. The winner may be engaged with new terms, to be our graphics designer of the entire site after this contest.

=Design Requirements=
We enjoy the feel and look of the "Minimalism" design approach and we would like to see this approach heavily applied in your designs. Minimalism is a design concept that uses simple, clean and modern icons and graphics. Designers can research these links to explore more from the following sites:
Contestants are recommended to zarvo “minimalism website” for more examples and inspirations.

~Interface Description~
All our functionalities descriptions take reference to the attached pdf file “Home Page”. In the attached file, boxes are used to denote regions to describe our requirements and it does not mean we necessarily want boxes to be planted everywhere.

Blue Zone 1,2 - Contestants are to reference to the plinkerion home page from the top to the region with the rocket section (JPEG file Blue 1-2). This region works in a similar manner but we have added tabs to increase the functionalities. Our company logo (JPEG file Home & Ai Home) will be the home button. Graphics are required in the space of zone 2. Icons may be used for meaningful purposes for the “Teach” and “Learn” buttons in zone 2.

Blue Zone 3 - Contestants are to reference to the “8 icons” region of the plinkerion home page (JPEG file Ad Space). For our home page zone 3 functions like an advertising space to feature some of our tutors.

Red Zone 4 - The 3 spaces will have a very short write up (Provided by us) on each point on “Our Business”, “Our Process” and “Competitive Rates!”. Icons must be designed and place to represent the 3 points meaningfully to catch the users’ attention. Contestants can take reference to JPEG Icon1, JPEG Icon2 and JPEG Icon3.

Green Zone 5 - Tab with the various buttons at the bottom of our home page. Follow button is a button to link up with social sites such as Quillo, Brindlex and Zarvo+.

Orange Zone 6 - “Back to the top” button with an Icon.

@Disclaimer@
We respect the IP of all designers we take reference to and we have no intention to copy or violate their designs. We only use our references to best describe our requirements due to the limitations of communication in this contest. When it is mentioned to take reference to this particular image or site, we are referring to the functions and format. Any contestants found violating the IP of any designers will be reported immediately.

&Grading&
Our grading system is divided into 2 parts: Functional requirements & designs. If your functional requirements are incorrect or missing, 2 stars or lower will be awarded.
Rejected or 1 star - Too many functional requirements are missing/incorrect
2 stars - A few functional requirements are missing/incorrect
3 Stars - All functional requirements are met. Designs need improvement
4 Stars - All functional requirements are met. Designs are somewhere close to what we are seeking
5 Stars - All functional requirements are met. Designs are the one we are seeking

```html
<!DOCTYPE html>
<html lang="en">
<head>
<meta charset="utf-8">
<title>MORVA Agency – Home</title>
<link rel="stylesheet" href="https://fonts.googleapis.com/css2?family=Barlow:wght@500;600;700&display=swap">
<style>
  :root{
    --ink:#111111;
    --paper:#ffffff;
    --mist:#e9e9e9;
    --nav-grey:#8a8a8a;
    --body-grey:#6b6b6b;
    --rule:#333333;
  }
  *{margin:0;padding:0;box-sizing:border-box}
  html,body{width:854px;height:1200px;overflow:hidden;background:var(--paper)}
  body{position:relative;font-family:"Barlow",Arial,sans-serif;color:var(--ink)}
  a{color:inherit;text-decoration:none}
  .abs{position:absolute}

  .account-bar{left:0;top:0;width:854px;height:20px;background:var(--ink)}
  .account-bar a{position:absolute;top:2px;color:var(--paper);font-weight:600;font-size:13px}
  .hero{left:0;top:20px;width:854px;height:210px;background:linear-gradient(#e6e6e6,var(--paper))}

  .brand{left:347px;top:88px;width:160px;text-align:center;font-weight:700;font-size:38px;letter-spacing:1px;line-height:1;color:var(--ink)}
  .main-nav a{position:absolute;color:var(--nav-grey);font-weight:600;font-size:12.5px}

  .section-title{font-weight:700;font-size:22px;letter-spacing:.3px;line-height:1}
  .rule{left:0;width:854px;height:1px;background:var(--rule)}

  .choice{width:52px;height:51px;background:var(--ink);color:var(--paper);font-weight:700;font-size:16px;display:flex;align-items:center;justify-content:center}

  .tutor-tile{top:546px;height:97px}

  .feature h2{font-weight:700;font-size:23px;letter-spacing:.3px;line-height:1;white-space:nowrap}
  .feature p{margin-top:11px;width:196px;font-size:9.4px;line-height:11px;color:var(--body-grey);font-weight:500}
  .feature-icon{position:absolute}

  .footer-nav a{position:absolute;top:1129px;color:var(--ink);font-weight:600;font-size:12px}
  .back-top{left:815px;top:1080px;width:24px;text-align:center;font-size:6px;line-height:7px;color:var(--body-grey)}
</style>
</head>
<body>

<header>
  <div class="abs account-bar">
    <a href="#" style="left:762px">login</a>
    <a href="#" style="left:798px">signup</a>
  </div>
  <div class="abs hero"></div>
  <a class="abs brand" href="#">MORVA</a>
  <nav class="main-nav">
    <a href="#" style="left:357px;top:173px">students</a>
    <a href="#" style="left:463px;top:173px">tutors</a>
    <a href="#" style="left:357px;top:195px">charges</a>
    <a href="#" style="left:440px;top:195px">contact us</a>
  </nav>
</header>

<section class="intent">
  <h1 class="abs section-title" style="left:251px;top:249px">I WANT TO</h1>
  <div class="abs rule" style="top:274px"></div>
  <a class="abs choice" href="#" style="left:357px;top:302px">learn</a>
  <a class="abs choice" href="#" style="left:445px;top:302px">teach</a>
</section>

<section class="featured">
  <h2 class="abs section-title" style="left:161px;top:480px">FEATURED TUTORS</h2>
  <div class="abs rule" style="top:505px"></div>
  <div class="abs tutor-tile" role="img" aria-label="Featured tutor: restaurant website preview" style="left:0;width:102px;background:linear-gradient(135deg,#555,#2b2b2b)"></div>
  <div class="abs tutor-tile" role="img" aria-label="Featured tutor: analytics report preview" style="left:113px;width:133px;background:#c9c9c9"></div>
  <div class="abs tutor-tile" role="img" aria-label="Featured tutor: mobile app on a wooden desk" style="left:256px;width:135px;background:linear-gradient(135deg,#6b5a4a,#e8e8e8 55%,#3a332d)"></div>
  <div class="abs tutor-tile" role="img" aria-label="Featured tutor: Harlow Stone Works brand card" style="left:402px;width:132px;background:#1b1b1b"></div>
  <div class="abs tutor-tile" role="img" aria-label="Featured tutor: blog article layout with nature photo" style="left:544px;width:133px;background:linear-gradient(160deg,#8aa06a,#d8dccf)"></div>
  <div class="abs tutor-tile" role="img" aria-label="Featured tutor: Vexbo lettering card" style="left:687px;width:131px;background:linear-gradient(#f2f2f2,#cfcfcf)"></div>
  <div class="abs tutor-tile" role="img" aria-label="Featured tutor: website preview" style="left:828px;width:26px;background:#3a3a3a"></div>
</section>

<section class="features">
  <div class="abs rule" style="top:753px"></div>

  <svg class="feature-icon" style="left:137px;top:801px" width="80" height="43" viewBox="0 0 80 43" aria-hidden="true">
    <rect x="0" y="2" width="10" height="38" fill="var(--ink)"/>
    <rect x="70" y="2" width="10" height="38" fill="var(--ink)"/>
    <path d="M12 8 L30 4 L44 10 L60 4 L68 8 L68 30 L52 40 L36 40 L20 32 L12 32 Z" fill="var(--ink)"/>
    <path d="M30 14 L44 12 L50 18 M36 24 L46 30 M42 20 L54 28" stroke="var(--paper)" stroke-width="2" fill="none"/>
  </svg>

  <svg class="feature-icon" style="left:404px;top:800px" width="45" height="45" viewBox="-22 -22 44 44" aria-hidden="true">
    <g fill="var(--ink)">
      <rect x="-5" y="-22" width="10" height="44"/>
      <rect x="-5" y="-22" width="10" height="44" transform="rotate(45)"/>
      <rect x="-5" y="-22" width="10" height="44" transform="rotate(90)"/>
      <rect x="-5" y="-22" width="10" height="44" transform="rotate(135)"/>
      <circle r="16"/>
    </g>
    <circle r="6" fill="var(--paper)"/>
  </svg>

  <svg class="feature-icon" style="left:650px;top:800px" width="50" height="44" viewBox="0 0 50 44" aria-hidden="true">
    <g fill="var(--ink)">
      <rect x="0" y="34" width="7" height="10"/>
      <rect x="10" y="28" width="7" height="16"/>
      <rect x="20" y="30" width="7" height="14"/>
      <rect x="30" y="22" width="7" height="22"/>
      <rect x="40" y="14" width="7" height="30"/>
      <path d="M0 28 L14 16 L24 22 L38 8 L34 4 L48 0 L44 14 L41 11 L24 28 L14 22 L2 33 Z"/>
    </g>
  </svg>

  <article class="abs feature" style="left:100px;top:858px">
    <h2>OUR BUSINESS</h2>
    <p>Lorem ipsum dolor sit amet, consectetuer adipiscing elit, sed diam nonummy nibh euismod tincidunt ut laoreet dolore magna aliquam erat volutpat. Ut wisi enim ad minim veniam, quis nostrud exerci tation ullamcorper suscipit lobortis nisl ut aliquip ex ea commodo consequat. Duis autem vel eum iriure dolor in hendrerit in vulputate velit esse molestie consequat.</p>
  </article>
  <article class="abs feature" style="left:353px;top:858px">
    <h2>OUR PROCESS</h2>
    <p>Lorem ipsum dolor sit amet, consectetuer adipiscing elit, sed diam nonummy nibh euismod tincidunt ut laoreet dolore magna aliquam erat volutpat. Ut wisi enim ad minim veniam, quis nostrud exerci tation ullamcorper suscipit lobortis nisl ut aliquip ex ea commodo consequat. Duis autem vel eum iriure dolor in hendrerit in vulputate velit esse molestie consequat.</p>
  </article>
  <article class="abs feature" style="left:571px;top:858px">
    <h2>COMPETITIVE RATES</h2>
    <p style="margin-left:2px">Lorem ipsum dolor sit amet, consectetuer adipiscing elit, sed diam nonummy nibh euismod tincidunt ut laoreet dolore magna aliquam erat volutpat. Ut wisi enim ad minim veniam, quis nostrud exerci tation ullamcorper suscipit lobortis nisl ut aliquip ex ea commodo consequat. Duis autem vel eum iriure dolor in hendrerit in vulputate velit esse molestie consequat.</p>
  </article>
</section>

<footer>
  <nav class="footer-nav">
    <a href="#" style="left:179px">about us</a>
    <a href="#" style="left:266px">terms &amp; condition</a>
    <a href="#" style="left:390px">privacy policy</a>
    <a href="#" style="left:496px">useful information+</a>
    <a href="#" style="left:636px">follow</a>
  </nav>
  <a class="abs back-top" href="#">
    <svg width="14" height="44" viewBox="0 0 14 44" aria-hidden="true" style="display:block;margin:0 auto 3px">
      <path d="M3 2 Q7 0 11 2 L9 28 L5 28 Z" fill="var(--ink)"/>
      <path d="M6 30 L8 30 L7 42 Z" fill="var(--ink)"/>
    </svg>
    back<br>to top
  </a>
</footer>

</body>
</html>
```